I have a small construction company that is growing. I specialize in commercial concrete and custom

I want a site that shows what we do. We specialize in custom deck design and builds. Custom home builds. Commercial concrete . project management

Target Market(s)

Commercial construction companies and custom home builders

Industry/Entity Type

Construction

Number of Pages Required

1 page

Font styles to use
Serif

Colors

Designer to choose colors to be used in the design.

Requirements
Must have
• Pictures and videos of project that we have completed or are in progress

```html
<!DOCTYPE html>
<html lang="en">
<head>
<meta charset="utf-8">
<title>Construction Company</title>
<link href="https://fonts.googleapis.com/css2?family=Lato:wght@400;700;900&display=swap" rel="stylesheet">
<style>
:root{
  --yellow:#f7c21a;
  --black:#0d0d0d;
  --ink:#222;
  --grey:#555;
  --line:#f7c21a;
  --white:#fff;
  --footer:#161616;
}
*{box-sizing:border-box;margin:0;padding:0}
html,body{width:1200px;height:4569px;overflow:hidden}
body{position:relative;background:var(--white);font-family:"Lato",Arial,sans-serif;color:var(--ink)}
.btn{position:absolute;background:var(--yellow);color:var(--black);font-size:14px;font-weight:700;border-radius:16px;text-align:center;line-height:32px;height:32px;width:128px}
.divider{position:absolute;left:122px;width:959px;height:2px;background:var(--line)}
.section-title{position:absolute;left:0;width:1200px;text-align:center;font-size:30px;font-weight:400;color:var(--ink);letter-spacing:1px}
.section-title b{position:relative;font-weight:900}
.section-title b::after{content:"";position:absolute;left:-14px;right:-14px;top:-16px;bottom:-8px;border:2px solid var(--yellow)}
.section-title b.plain{font-weight:400}
.arrows{position:absolute;left:1025px;display:flex;gap:6px}
.arrows span{width:24px;height:24px;display:block}
.arrows .prev{background:var(--black)}
.arrows .next{background:var(--yellow)}
.arrows svg{display:block}
.photo{position:absolute}

/* nav */
.nav{position:absolute;top:0;left:0;width:1200px;height:76px;background:var(--black)}
.brand{position:absolute;left:91px;top:0;width:229px;height:76px;background:var(--yellow);font-size:34px;font-weight:700;color:var(--black);padding:18px 0 0 16px}
.menu{position:absolute;left:366px;top:28px;display:flex;gap:26px;font-size:14px}
.menu span{color:#e8c65a}
.menu .active{color:var(--white);font-weight:700}
.notch{position:absolute;left:384px;top:0;width:0;height:0;border-left:12px solid transparent;border-right:12px solid transparent;border-top:12px solid var(--white)}
.quote-btn{position:absolute;left:981px;top:25px;width:100px;height:26px;border-radius:13px;background:var(--yellow);font-size:11px;font-weight:700;text-align:center;line-height:26px;color:var(--black)}

/* hero */
.hero{position:absolute;top:76px;left:0;width:1200px;height:554px;background:linear-gradient(180deg,#2c5d8a 0%,#3f78a6 45%,#44606f 75%,#2f3a2f 100%)}
.hero-title{position:absolute;top:220px;width:1200px;text-align:center;font-size:50px;font-weight:400;color:var(--white);letter-spacing:2px}
.hero-title b{color:var(--yellow);font-weight:900}
.hero-sub{position:absolute;top:292px;width:1200px;text-align:center;font-size:15px;color:var(--white)}

/* stats */
.stats{position:absolute;top:630px;left:0;width:1200px;height:138px;background:var(--black)}
.stats .map{position:absolute;left:244px;top:10px;width:190px;height:118px;background:radial-gradient(ellipse at center,#3a3a3a 0%,#1a1a1a 70%,transparent 100%)}
.stats .count{position:absolute;left:277px;top:48px;font-size:38px;font-weight:700;color:var(--yellow)}
.stats .label{position:absolute;left:509px;top:42px;font-size:20px;color:var(--white);letter-spacing:1px}
.stats .label b{font-weight:900}
.stats .text{position:absolute;left:509px;top:74px;font-size:15px;color:var(--white)}

/* services */
.worker{left:228px;top:883px;width:259px;height:366px;background:linear-gradient(180deg,#f1f1f1 0%,#d9d9d9 40%,#1f2a44 70%,#1f2a44 100%)}
.spec-rule{position:absolute;left:597px;top:914px;width:2px;height:290px;background:var(--black)}
.spec-title{position:absolute;left:615px;top:948px;font-size:28px;font-weight:700;color:var(--black)}
.spec-text{position:absolute;left:615px;top:990px;font-size:14px;color:var(--grey)}
.spec-grid{position:absolute;left:630px;top:1036px;width:451px;height:167px;display:grid;grid-template-columns:1fr 1fr;grid-template-rows:1fr 1fr}
.spec-grid::before{content:"";position:absolute;left:225px;top:0;width:2px;height:100%;background:var(--black)}
.spec-grid::after{content:"";position:absolute;left:0;top:83px;width:100%;height:2px;background:var(--black)}
.spec-item{display:flex;align-items:center;gap:14px;padding-left:30px;font-size:13px;color:var(--ink);line-height:1.3}
.spec-item.first{color:#c99a08}
.spec-item svg{flex:none}

/* projects */
.projects{position:absolute;top:1432px;left:0;width:1200px;height:246px;display:flex}
.tile{width:300px;height:246px;position:relative}
.tile.t1{background:linear-gradient(160deg,#8fb4d8 0%,#c7ccd1 55%,#7c8288 100%)}
.tile.t2{background:linear-gradient(170deg,#2f6fb4 0%,#6ea1d2 50%,#8c949b 100%)}
.tile.t3{background:var(--yellow)}
.tile.t4{background:linear-gradient(170deg,#5d8fc4 0%,#a7c4de 45%,#8e7a63 75%,#6d8a52 100%)}
.tile.t3 .name{position:absolute;left:18px;top:20px;font-size:26px;font-weight:700;color:var(--black)}
.tile.t3 .loc{position:absolute;left:18px;top:54px;font-size:15px;color:var(--black)}
.tile.t3 svg{position:absolute;left:132px;top:104px}

/* about */
.about-title{position:absolute;left:122px;top:1910px;font-size:30px;color:var(--ink)}
.about-title b{position:relative;font-weight:900}
.about-title b::after{content:"";position:absolute;left:-10px;right:-14px;top:-16px;bottom:-8px;border:2px solid var(--yellow)}
.about-text{position:absolute;left:122px;top:2000px;width:470px;font-size:13.5px;line-height:1.45;color:var(--grey)}
.video{position:absolute;left:634px;top:1873px;width:441px;height:244px;border:5px solid var(--yellow);background:linear-gradient(135deg,#8d8d8d 0%,#5c5c5c 50%,#9a9a9a 100%)}
.video svg{position:absolute;left:180px;top:80px}

/* testimonials */
.tcard{position:absolute;background:var(--black);color:var(--white);text-align:center}
.tcard.mid{background:var(--yellow);color:var(--black)}
.tcard .q{position:absolute;left:16px;top:8px;font-size:56px;font-weight:900;line-height:1;color:inherit}
.avatar{position:absolute;border-radius:50%;border:4px solid var(--yellow);background:radial-gradient(circle at 50% 40%,#c9c2b8,#7d7670)}
.tcard .name{font-size:19px;font-weight:700;margin-top:70px}
.tcard .role{font-size:12px;margin-top:2px}
.tcard .stars{font-size:11px;color:var(--yellow);letter-spacing:2px;margin-top:4px}
.tcard.mid .stars{color:var(--black)}
.tcard .body{font-size:13px;line-height:1.4;margin:8px auto 0;width:240px}
.tcard .more{font-size:13px;margin-top:12px}
.dots{position:absolute;left:0;width:1200px;display:flex;justify-content:center;gap:12px}
.dots i{width:14px;height:14px;border-radius:50%;background:var(--black);display:block}
.dots i.on{background:var(--yellow)}

/* blogs */
.blog{position:absolute;top:2961px;width:295px;height:414px}
.blog .img{position:absolute;left:0;top:0;width:295px;height:210px}
.blog .panel{position:absolute;left:0;top:210px;width:295px;height:204px;background:var(--black);color:var(--white);text-align:center}
.blog.mid .panel{background:var(--yellow);color:var(--black)}
.blog .date{position:absolute;left:112px;top:-38px;width:72px;height:72px;border-radius:50%;background:var(--white);border:3px solid var(--yellow);color:var(--black);text-align:center;padding-top:10px}
.blog .date b{display:block;font-size:22px;line-height:1}
.blog .date small{font-size:9px}
.blog h3{font-size:24px;font-weight:900;margin-top:48px}
.blog p{font-size:13px;line-height:1.4;width:240px;margin:8px auto 0}
.blog .meta{position:absolute;left:30px;right:30px;bottom:18px;display:flex;justify-content:space-between;font-size:13px}

/* subscribe */
.sub-text{position:absolute;top:3676px;width:1200px;text-align:center;font-size:13px;letter-spacing:.5px;color:var(--ink)}
.sub-form{position:absolute;left:359px;top:3722px;width:485px;height:43px;border:2px solid #333;border-radius:22px;overflow:hidden;background:var(--white)}
.sub-form span{position:absolute;left:22px;top:12px;font-size:13px;color:#777}
.sub-form i{position:absolute;right:0;top:0;width:74px;height:100%;background:var(--yellow)}
.sub-form svg{position:absolute;right:26px;top:11px}

/* clients */
.clients{position:absolute;left:122px;top:4005px;width:959px;height:80px;display:flex;align-items:center}
.client{flex:1;display:flex;align-items:center;justify-content:center;font-size:19px;font-weight:700;color:var(--ink);border-right:2px solid #cfcfcf;height:70px}
.client:last-child{border-right:none}

/* footer */
.footer{position:absolute;left:0;top:4136px;width:1200px;height:433px;background:linear-gradient(135deg,#1e1e1e 0%,#121212 55%,#242424 100%);color:var(--white)}
.f-h{position:absolute;font-size:20px;font-weight:700}
.f-t{position:absolute;font-size:15px;line-height:1.4}
.f-sep{position:absolute;top:26px;width:2px;height:70px;background:var(--white)}
.f-logo{position:absolute;left:122px;top:165px;font-size:34px;font-weight:900;color:var(--yellow)}
.f-links{position:absolute;left:518px;top:210px;font-size:13px;line-height:1.5}
.f-input{position:absolute;left:786px;top:215px;width:295px;height:26px;border-radius:13px;background:var(--white);overflow:hidden}
.f-input span{position:absolute;left:12px;top:6px;font-size:10px;color:#666}
.f-input i{position:absolute;right:0;top:0;width:52px;height:26px;background:var(--yellow)}
.f-input svg{position:absolute;right:18px;top:6px}
.f-bottom{position:absolute;left:0;top:366px;width:1200px;height:67px;border-top:1px solid #444}
.f-copy{position:absolute;left:122px;top:22px;font-size:14px}
.social{position:absolute;left:966px;top:14px;display:flex;gap:10px}
.social i{width:30px;height:30px;border-radius:50%;border:2px solid var(--white);display:block}
</style>
</head>
<body>

<header class="nav">
  <div class="brand">Your Logo</div>
  <div class="notch"></div>
  <nav class="menu">
    <span class="active">HOME</span>
    <span>ABOUT</span>
    <span>SERVICES ▾</span>
    <span>PROJECTS</span>
    <span>TESTIMONIALS</span>
    <span>BLOGS</span>
    <span>CONTACT</span>
  </nav>
  <div class="quote-btn">GET A QUOTE</div>
</header>

<section class="hero" role="img" aria-label="Construction site with tower cranes and scaffolding against a blue sky">
  <h1 class="hero-title">WE <b>INNOVATE</b></h1>
  <p class="hero-sub">Lorem Ipsum is simply dummy text of the printing and typesetting industry</p>
  <div class="btn" style="left:536px;top:340px">Read More</div>
</section>

<section class="stats">
  <div class="map" role="img" aria-label="Faint world map"></div>
  <div class="count">4,590</div>
  <div class="label">COMPLETE <b>PROJECTS</b></div>
  <div class="text">Lorem Ipsum is simply dummy text of the printing and typesetting industry.</div>
</section>

<h2 class="section-title" style="top:820px">OUR <b>SERVICES</b></h2>
<div class="photo worker" role="img" aria-label="Smiling builder in a yellow hard hat with arms crossed"></div>
<div class="spec-rule"></div>
<h3 class="spec-title">We Specialize In</h3>
<p class="spec-text">Lorem Ipsum is simply dummy text of the printing and typesetting industry.</p>
<div class="spec-grid">
  <div class="spec-item first">
    <svg width="34" height="30" viewBox="0 0 34 30" fill="none" stroke="#c99a08" stroke-width="2"><path d="M2 12h30M4 12v16M30 12v16M4 20h26M9 12V4h16v8"/></svg>
    <span>Custom Deck<br>Design &amp; Build</span>
  </div>
  <div class="spec-item">
    <svg width="34" height="30" viewBox="0 0 34 30" fill="none" stroke="#222" stroke-width="2"><path d="M6 24l10-14 10 6M16 10l4-6M4 26h24"/><circle cx="26" cy="20" r="4"/></svg>
    <span>Commercial<br>Concrete</span>
  </div>
  <div class="spec-item">
    <svg width="34" height="30" viewBox="0 0 34 30" fill="none" stroke="#222" stroke-width="2"><path d="M3 14L17 3l14 11M7 11v16h20V11M14 27v-8h6v8"/></svg>
    <span>Custom home builds</span>
  </div>
  <div class="spec-item">
    <svg width="34" height="30" viewBox="0 0 34 30" fill="none" stroke="#222" stroke-width="2"><path d="M4 26h26M8 26V16M15 26V10M22 26V14M29 26V6"/></svg>
    <span>Project<br>Management</span>
  </div>
</div>
<div class="divider" style="top:1249px"></div>

<h2 class="section-title" style="top:1323px">OUR <b>PROECTS</b></h2>
<div class="arrows" style="top:1331px">
  <span class="prev"><svg width="24" height="24"><path d="M14 7l-5 5 5 5" fill="none" stroke="#fff" stroke-width="2.5"/></svg></span>
  <span class="next"><svg width="24" height="24"><path d="M10 7l5 5-5 5" fill="none" stroke="#000" stroke-width="2.5"/></svg></span>
</div>
<section class="projects">
  <div class="tile t1" role="img" aria-label="Modern glass office building"></div>
  <div class="tile t2" role="img" aria-label="High-rise towers under blue sky"></div>
  <div class="tile t3">
    <div class="name">Company Name</div>
    <div class="loc">Location</div>
    <svg width="36" height="36" viewBox="0 0 36 36" fill="none" stroke="#000" stroke-width="3"><path d="M2 12V2h10M24 2h10v10M34 24v10H24M12 34H2V24"/><circle cx="18" cy="18" r="6"/></svg>
  </div>
  <div class="tile t4" role="img" aria-label="Two-storey family house with lawn"></div>
</section>
<div class="btn" style="left:536px;top:1729px">View More</div>
<div class="divider" style="top:1809px"></div>

<h2 class="about-title">ABOUT <b>US</b></h2>
<p class="about-text">Lorem Ipsum is simply dummy text of the printing and typesetting industry. Lorem Ipsum has been the industry's standard dummy text ever since the 1500s, when an unknown printer took a galley of type and scrambled it to make a type specimen book.</p>
<div class="video" role="img" aria-label="Video of a concrete site seen from above">
  <svg width="70" height="70" viewBox="0 0 70 70"><circle cx="35" cy="35" r="32" fill="rgba(0,0,0,.35)" stroke="#fff" stroke-width="3"/><path d="M28 22l20 13-20 13z" fill="#fff"/></svg>
</div>
<div class="divider" style="top:2175px"></div>

<h2 class="section-title" style="top:2240px">Te<b class="plain">timonials</b></h2>
<div class="arrows" style="top:2248px">
  <span class="prev"><svg width="24" height="24"><path d="M14 7l-5 5 5 5" fill="none" stroke="#fff" stroke-width="2.5"/></svg></span>
  <span class="next"><svg width="24" height="24"><path d="M10 7l5 5-5 5" fill="none" stroke="#000" stroke-width="2.5"/></svg></span>
</div>
<div class="tcard" style="left:122px;top:2412px;width:301px;height:223px">
  <div class="q">“</div>
  <div class="name">Daniel Reed</div><div class="role">Client</div><div class="stars">★★★★★</div>
  <p class="body">Lorem Ipsum is simply dummy text of the printing and typesetting industry.</p>
  <div class="more">Read More... »</div>
</div>
<div class="avatar" style="left:219px;top:2350px;width:106px;height:106px" role="img" aria-label="Client portrait"></div>
<div class="tcard mid" style="left:442px;top:2391px;width:320px;height:256px">
  <div class="q">“</div>
  <div class="name" style="margin-top:100px">Joel Archer</div><div class="role">Client</div><div class="stars">★★★★★</div>
  <p class="body">Lorem Ipsum is simply dummy text of the printing and typesetting industry.</p>
  <div class="more">Read More... »</div>
</div>
<div class="avatar" style="left:531px;top:2338px;width:142px;height:142px;border-color:var(--black)" role="img" aria-label="Client portrait"></div>
<div class="tcard" style="left:783px;top:2412px;width:298px;height:223px">
  <div class="q">“</div>
  <div class="name">Maya Kent</div><div class="role">Client</div><div class="stars">★★★★★</div>
  <p class="body">Lorem Ipsum is simply dummy text of the printing and typesetting industry.</p>
  <div class="more">Read More... »</div>
</div>
<div class="avatar" style="left:879px;top:2350px;width:106px;height:106px" role="img" aria-label="Client portrait"></div>
<div class="dots" style="top:2677px"><i></i><i class="on"></i><i></i></div>
<div class="btn" style="left:536px;top:2725px">View More</div>
<div class="divider" style="top:2796px"></div>

<h2 class="section-title" style="top:2862px">OUR LATEST <b>BLOGS</b></h2>
<div class="arrows" style="top:2870px">
  <span class="prev"><svg width="24" height="24"><path d="M14 7l-5 5 5 5" fill="none" stroke="#fff" stroke-width="2.5"/></svg></span>
  <span class="next"><svg width="24" height="24"><path d="M10 7l5 5-5 5" fill="none" stroke="#000" stroke-width="2.5"/></svg></span>
</div>
<article class="blog" style="left:128px">
  <div class="img" role="img" aria-label="Building frame under construction with a crane" style="background:linear-gradient(180deg,#3f86d6 0%,#7fb1e3 50%,#8a4b2e 100%)"></div>
  <div class="panel"><div class="date"><b>21</b><small>March 2018</small></div>
    <h3>TITLE 1</h3><p>Lorem Ipsum is simply dummy text of the printing and typesetting industry.</p>
    <div class="meta"><span>Read More... »</span><span>♡ 20 &nbsp;◯ 20</span></div></div>
</article>
<article class="blog mid" style="left:454px">
  <div class="img" role="img" aria-label="Timber-framed house under construction" style="background:linear-gradient(180deg,#6aa0d4 0%,#a9c4de 40%,#7b6a58 100%)"></div>
  <div class="panel"><div class="date"><b>22</b><small>March 2018</small></div>
    <h3>TITLE 2</h3><p>Lorem Ipsum is simply dummy text of the printing and typesetting industry.</p>
    <div class="meta"><span>Read More... »</span><span>♡ 20 &nbsp;◯ 20</span></div></div>
</article>
<article class="blog" style="left:780px">
  <div class="img" role="img" aria-label="Colourful apartment block" style="background:linear-gradient(180deg,#4c8fd6 0%,#9cc1e6 40%,#d9a24c 70%,#8da4b8 100%)"></div>
  <div class="panel"><div class="date"><b>23</b><small>March 2018</small></div>
    <h3>TITLE 3</h3><p>Lorem Ipsum is simply dummy text of the printing and typesetting industry.</p>
    <div class="meta"><span>Read More... »</span><span>♡ 20 &nbsp;◯ 20</span></div></div>
</article>
<div class="dots" style="top:3423px"><i></i><i class="on"></i><i></i></div>
<div class="btn" style="left:536px;top:3469px">View More</div>

<h2 class="section-title" style="top:3611px"><b>SUBSCRIBE</b></h2>
<p class="sub-text">SUBSCRIBE TO OUR NEWSLETTER</p>
<div class="sub-form"><span>Your E-Mail Here</span><i></i>
  <svg width="22" height="20" viewBox="0 0 22 20"><path d="M1 10L21 1 15 19 11 12z" fill="#000"/></svg>
</div>
<div class="divider" style="top:3832px"></div>

<h2 class="section-title" style="top:3903px">OUR <b>CLIENTS</b></h2>
<div class="clients">
  <div class="client">Tidewater Group</div>
  <div class="client">Northgate Supply</div>
  <div class="client">Pinecrest</div>
  <div class="client">Marlow Homes</div>
  <div class="client">Halden Partners</div>
</div>

<footer class="footer">
  <div class="f-h" style="left:122px;top:32px">Call Us Now</div>
  <div class="f-t" style="left:122px;top:62px">202-555-0147</div>
  <div class="f-sep" style="left:386px"></div>
  <div class="f-h" style="left:518px;top:32px">Come Visit Now</div>
  <div class="f-t" style="left:518px;top:62px">48 Harbor Ave. Coral Bay,<br>FL 32900</div>
  <div class="f-sep" style="left:816px"></div>
  <div class="f-h" style="right:119px;top:32px;text-align:right">Send Massage</div>
  <div class="f-t" style="right:119px;top:62px;text-align:right">info@stonecrestbuild.com</div>

  <div class="f-logo">YOUR LOGO</div>
  <div class="f-t" style="left:122px;top:214px;width:230px;font-size:14px">Lorem Ipsum is simply dummy text of the printing and typesetting industry.</div>
  <div class="f-t" style="left:122px;top:312px;font-size:14px">Read More... »</div>

  <div class="f-h" style="left:518px;top:176px;font-size:24px">Quick Link</div>
  <div class="f-links">HOME<br>ABOUT US<br>SERVICES<br>PROJECTS<br>TESTIMONIALS<br>BLOGS<br>CONTACT US</div>

  <div class="f-h" style="left:786px;top:160px;font-size:24px">Subscribe Now</div>
  <div class="f-input"><span>Your E-Mail Here</span><i></i>
    <svg width="16" height="14" viewBox="0 0 22 20"><path d="M1 10L21 1 15 19 11 12z" fill="#000"/></svg>
  </div>

  <div class="f-bottom">
    <div class="f-copy">CopyRight © 2018 company name. All Right Reserve</div>
    <div class="social"><i></i><i></i><i></i></div>
  </div>
</footer>

</body>
</html>
```